LLC needs a business card design that emphasizes consulting and expert witness in upstream oil and g

I need a business card design for my company called Kelvora Consultative Service, LLC. My expertise is in oil and gas upstream operations management to optimize performance and also as an expert witness for law firms in oil and gas upstream operations litigation.
The final design should communicate knowledge and hands-on experience as well as trust. (Kelvora means rope or lasso. Perhaps "Kelvora" should be in the form of a rope.) I do not like the color green in any shade. My first preference would be some shade of blue.
Oil And Gas

```html
<!DOCTYPE html>
<html lang="en">
<head>
<meta charset="utf-8">
<title>Kelvora Consultative Service, LLC – Business Card</title>
<link href="https://fonts.googleapis.com/css2?family=Lato:wght@400;700&display=swap" rel="stylesheet">
<style>
  :root {
    --backdrop: #3b3734;
    --card: #1c1c1d;
    --card-edge: #2a2a2b;
    --gold: #f2b51c;
    --white: #f1f1f1;
    --silver: #d6d6d6;
    --muted: #b9b9b9;
    --rule: #3c3c3e;
  }
  * { margin: 0; padding: 0; box-sizing: border-box; }
  html, body {
    width: 1200px; height: 844px; overflow: hidden;
    background: var(--backdrop);
    font-family: "Lato", Arial, sans-serif;
  }
  .sheet {
    position: relative; width: 1200px; height: 844px;
    display: flex; align-items: center; justify-content: center; gap: 50px;
  }
  .card {
    width: 525px; height: 300px;
    background: var(--card);
    border: 1px solid var(--card-edge);
    position: relative;
  }
  /* Front */
  .card-front { display: flex; align-items: center; }
  .front-brand {
    width: 250px; text-align: center;
    color: var(--gold); font-weight: 700; font-size: 50px; letter-spacing: 1px;
  }
  .front-divider {
    width: 1px; height: 150px; background: var(--rule);
  }
  .contact { padding-left: 26px; color: var(--white); font-size: 16px; line-height: 1.35; }
  .contact-name { color: var(--gold); font-weight: 700; font-size: 19px; }
  .contact-role { margin-bottom: 16px; }
  .contact-label { color: var(--gold); }
  .contact-address { margin-top: 16px; }
  /* Back */
  .card-back {
    display: flex; flex-direction: column; align-items: center; justify-content: center;
    text-align: center;
  }
  .back-brand { color: var(--silver); font-weight: 700; font-size: 60px; line-height: 1; }
  .back-tagline {
    color: var(--white); font-weight: 700; font-size: 19px;
    letter-spacing: 1px; text-transform: uppercase; margin-top: 8px;
  }
  .back-rule { width: 380px; height: 1px; background: var(--rule); margin: 18px 0 14px; }
  .services { color: var(--muted); font-size: 13px; line-height: 1.5; }
</style>
</head>
<body>
  <main class="sheet">
    <section class="card card-front" aria-label="Business card front">
      <div class="front-brand">Kelvora</div>
      <div class="front-divider"></div>
      <div class="contact">
        <p class="contact-name">Daniel Marwick, P.E.</p>
        <p class="contact-role">Managing Member</p>
        <p><span class="contact-label">T:</span> 713 555 0148</p>
        <p><span class="contact-label">E:</span> dmarwick@examplemail.net</p>
        <p class="contact-address"><span class="contact-label">A:</span> Midland, Texas USA.</p>
      </div>
    </section>

    <section class="card card-back" aria-label="Business card back">
      <div class="back-brand">Kelvora</div>
      <div class="back-tagline">Consultative Service, LLC</div>
      <div class="back-rule"></div>
      <div class="services">
        <p>Advisor to Upstream Operations Management and Expert</p>
        <p>Witness for Upstream Operations</p>
        <p>Licensed Professional Engineer in Texas #52870</p>
        <p>40+ years of hands-on experience both foreign and domestic.</p>
      </div>
    </section>
  </main>
</body>
</html>
```